2021 Summer Ads Whitmore Ash Custom Homes

We need a re-design of our summer ad run for our customer, Whitmore Ash Custom Homes. They are custom home builders in the mostly rural parts of West Virginia, USA. They are known for their "Forever Home" tagline. We'd like two designed ads with the main difference being just the custom home that's featured. These designs should be for a Google banner like 300 x 250 and square ad like 250 x 250. For inspiration please visit the Whitmore Ash Custom Homes website at www dot whitmoreashcustomhomes dot com

Target Market(s)

consumers / new home shoppers

Industry/Entity Type

Consumer

Requirements
Must have
• WACH logo
Price Lock Available!
Custom home pic
Learn more >
small QVTG logo mark

```html
<!DOCTYPE html>
<html lang="en">
<head>
<meta charset="utf-8">
<title>Whitmore Ash Custom Homes – Summer Banners</title>
<link rel="stylesheet" href="https://fonts.googleapis.com/css2?family=Montserrat:wght@500;600;800&display=swap">
<style>
  :root {
    --stage: #bdbdbd;
    --label: #3a3a3a;
    --brand-red: #c80000;
    --deep-red: #8f0f0f;
    --ink: #141414;
    --white: #ffffff;
  }
  * { box-sizing: border-box; margin: 0; padding: 0; }
  html, body { width: 1200px; height: 565px; overflow: hidden; }
  body {
    background: var(--stage);
    font-family: "Montserrat", Arial, sans-serif;
    position: relative;
  }
  .size-label {
    position: absolute;
    top: 42px;
    font-size: 11px;
    font-weight: 500;
    color: var(--label);
    letter-spacing: 0.2px;
  }
  .banner {
    position: absolute;
    top: 70px;
    height: 443px;
    overflow: hidden;
    background: var(--white);
    box-shadow: 0 3px 8px rgba(0,0,0,0.35);
  }
  .banner--wide { left: 77px; width: 531px; }
  .banner--square { left: 662px; width: 451px; }

  .home-photo {
    position: absolute;
    inset: 0;
  }
  .banner--wide .home-photo {
    background: linear-gradient(180deg,
      #ffffff 0%, #ffffff 24%, #e4edf2 36%, #a9bfa3 48%,
      #6f8f62 58%, #8f9a90 70%, #a9372a 80%, #b93b2c 88%, #d8cfc0 100%);
  }
  .banner--square .home-photo {
    background: linear-gradient(180deg,
      #ffffff 0%, #ffffff 20%, #cfe2ef 34%, #8fb8d6 42%,
      #4f8a3c 52%, #dfe3e0 66%, #3c4a3a 80%, #6b6f66 100%);
  }

  .brand-name {
    position: absolute;
    color: var(--brand-red);
    font-weight: 800;
    text-transform: uppercase;
    line-height: 1.1;
    text-align: center;
  }
  .banner--wide .brand-name { left: 22px; top: 36px; width: 180px; font-size: 17px; }
  .banner--square .brand-name { left: 16px; top: 32px; width: 150px; font-size: 14px; }

  .offer {
    position: absolute;
    top: 0;
    right: 0;
    background: var(--brand-red);
    color: var(--white);
    font-weight: 800;
    line-height: 0.92;
    letter-spacing: -0.5px;
    display: flex;
    flex-direction: column;
    justify-content: center;
    align-items: center;
    text-align: center;
  }
  .banner--wide .offer { width: 308px; height: 111px; font-size: 39px; }
  .banner--square .offer { width: 265px; height: 97px; font-size: 33px; }

  .footer-band {
    position: absolute;
    left: 0;
    bottom: 0;
    width: 100%;
    height: 120px;
  }
  .cta {
    position: absolute;
    bottom: 22px;
    color: var(--white);
    font-weight: 600;
    font-size: 20px;
    display: flex;
    align-items: center;
    gap: 12px;
  }
  .banner--wide .cta { left: 43px; }
  .banner--square .cta { left: 29px; }
  .cta-arrow { width: 11px; height: 18px; }

  .partner-mark {
    position: absolute;
    bottom: 30px;
    color: var(--white);
    font-weight: 800;
    font-size: 21px;
    letter-spacing: -0.5px;
  }
  .banner--wide .partner-mark { right: 22px; }
  .banner--square .partner-mark { right: 20px; }
</style>
</head>
<body>

  <p class="size-label" style="left:76px;">BANNER 300X250</p>
  <p class="size-label" style="left:661px;">BANNER 250X250</p>

  <!-- 300x250 -->
  <section class="banner banner--wide">
    <div class="home-photo" role="img" aria-label="Custom home with a red board-and-batten barn-style garage and white farmhouse wing, set against tall green trees"></div>
    <p class="brand-name">Whitmore Ash<br>Custom Homes</p>
    <h2 class="offer"><span>PRICE LOCK</span><span>AVAILABLE!</span></h2>
    <svg class="footer-band" viewBox="0 0 531 120" preserveAspectRatio="none" aria-hidden="true">
      <polygon points="0,7 264,48 531,7 531,120 0,120" fill="var(--ink)"/>
      <polygon points="0,0 264,41 531,0 531,7 264,48 0,7" fill="var(--brand-red)"/>
    </svg>
    <p class="cta">Learn more
      <svg class="cta-arrow" viewBox="0 0 11 18" aria-hidden="true"><polyline points="2,2 9,9 2,16" fill="none" stroke="var(--brand-red)" stroke-width="2.5"/></svg>
    </p>
    <p class="partner-mark">QVTG</p>
  </section>

  <!-- 250x250 -->
  <section class="banner banner--square">
    <div class="home-photo" role="img" aria-label="White board-and-batten custom home with cupola, covered porch, stone base and dark garage doors, surrounded by trees and flowering shrubs"></div>
    <p class="brand-name">Whitmore Ash<br>Custom Homes</p>
    <h2 class="offer"><span>PRICE LOCK</span><span>AVAILABLE!</span></h2>
    <svg class="footer-band" viewBox="0 0 451 120" preserveAspectRatio="none" aria-hidden="true">
      <polygon points="0,7 223,48 451,7 451,120 0,120" fill="var(--ink)"/>
      <polygon points="0,0 223,41 451,0 451,7 223,48 0,7" fill="var(--brand-red)"/>
    </svg>
    <p class="cta">Learn more
      <svg class="cta-arrow" viewBox="0 0 11 18" aria-hidden="true"><polyline points="2,2 9,9 2,16" fill="none" stroke="var(--brand-red)" stroke-width="2.5"/></svg>
    </p>
    <p class="partner-mark">QVTG</p>
  </section>

</body>
</html>
```